Home Services (heating, cooling, electrical, plumbing) postcard design

We are looking for postcards to way to send a brief written message to our clients. Most often these will be used by the sales team but there will be opportunity for our techs to reach out to their clients as well.
We don't want them to be sales-y so if the logo, name, or taglines are used we prefer it to be more subtle.
It also doesn't need to match our website design as we are looking for a more casual feel. Something nostalgic/retro/vintage might be fun.

About us: (PLEASE DO NOT USE ANY OF THE FOLLOWING PHRASING ON THE DESIGN, this information is just to give you an idea of who we are)
- a service company that focuses on heating, cooling, electrical and plumbing service and retrofit (residential and commercial)
- family owned
- based in Warman which is a smaller city in rural Saskatchewan
- we have used the tagline "ensuring your comfort, safety and health since 2009"
- values: gratitude, stewardship, teamwork, lifelong learning, communication, quality, service
- we are professional but not stuffy, we have a fun team
- we like to inform and educate our clients

Target Market(s)

clients that we have already engaged with, we are often reaching out to say thanks (for referrals, or for the opportunity to serve them)

Industry/Entity Type

HVAC (heating, ventilation, ac), electrical, plumbing

Requirements
Must have
• Enough room on the back of postcard for mailing address and larger blank space for a message.
Nice to have
• Original designs or artwork (try to avoid stock photos), vintage feel
Should not have
• prefer not to be sales-y or promotional, it's not meant to be about us, any use of BrelloVane logo or information should be subtle

```html
<!DOCTYPE html>
<html lang="en">
<head>
<meta charset="utf-8">
<title>BrelloVane Thank-You Postcard</title>
<link href="https://fonts.googleapis.com/css2?family=Montserrat:wght@400;500;600;700;800&display=swap" rel="stylesheet">
<style>
  :root {
    --orange: #f26522;
    --blue: #0f75bc;
    --paper: #f1f1f3;
    --ink: #4a4a4a;
    --rule: #8a8a8a;
    --stage: #1c1c1e;
    --white: #ffffff;
  }
  * { margin: 0; padding: 0; box-sizing: border-box; }
  html, body { width: 1200px; height: 848px; overflow: hidden; }
  body { background: var(--stage); font-family: "Montserrat", sans-serif; position: relative; }

  .card {
    position: absolute; top: 233px; width: 560px; height: 381px;
    background: var(--paper); overflow: hidden;
  }
  .card--front { left: 30px; }
  .card--back { left: 610px; }
  .card-shapes { position: absolute; inset: 0; width: 100%; height: 100%; }
  .abs { position: absolute; }

  /* front */
  .brand { left: 32px; top: 24px; }
  .brand-name { font-size: 25px; font-weight: 800; color: var(--blue); line-height: 1; letter-spacing: -0.5px; }
  .brand-tagline { font-size: 8.5px; font-weight: 500; color: var(--ink); margin-top: 5px; white-space: nowrap; }

  .hero { left: 300px; width: 270px; text-align: center; color: var(--white); }
  .hero-kicker { top: 31px; font-size: 22px; font-weight: 500; letter-spacing: 0.5px; }
  .hero-title { font-size: 38px; font-weight: 800; line-height: 1; }
  .hero-title--first { top: 72px; }
  .hero-title--second { top: 118px; }
  .hero-quote { top: 159px; font-size: 13.5px; font-weight: 500; line-height: 16px; }
  .hero-note { top: 201px; font-size: 9.5px; font-weight: 500; line-height: 12px; }

  .signoff { text-align: center; color: var(--white); }
  .signoff-label { font-size: 13px; font-weight: 700; }
  .signoff-number { font-size: 18px; font-weight: 700; margin-top: 3px; letter-spacing: 0.3px; }
  .card--front .signoff { left: 360px; width: 200px; top: 316px; }

  /* back */
  .section-title { font-size: 14px; font-weight: 500; color: var(--blue); letter-spacing: 0.2px; }
  .section-title strong { color: var(--orange); font-weight: 700; }
  .message { left: 25px; top: 31px; width: 262px; }
  .message-line { left: 25px; width: 262px; border-top: 1px dashed var(--rule); }
  .divider { left: 298px; top: 31px; width: 1px; height: 250px; background: var(--blue); }

  .stamp { left: 443px; top: 36px; width: 90px; height: 90px; border: 1px dashed #555; }
  .address-line { left: 312px; width: 221px; border-top: 1px dashed var(--rule); }

  .card--back .signoff { left: 25px; top: 320px; text-align: left; }

  .brand--small { left: 443px; top: 327px; }
  .brand--small .brand-name { font-size: 13px; }
  .brand--small .brand-tagline { font-size: 4.6px; margin-top: 3px; }
</style>
</head>
<body>

<section class="card card--front" aria-label="Postcard front">
  <svg class="card-shapes" viewBox="0 0 902 613" preserveAspectRatio="none" aria-hidden="true">
    <defs>
      <linearGradient id="heroGlow" x1="0" y1="0" x2="1" y2="1">
        <stop offset="0" stop-color="#e8621f"/>
        <stop offset="0.5" stop-color="#f06a24"/>
        <stop offset="1" stop-color="#c9581e"/>
      </linearGradient>
    </defs>
    <polygon points="395,0 902,0 902,405 545,405 362,75" fill="var(--blue)"/>
    <polygon points="420,0 902,0 902,380 560,380 387,75" fill="url(#heroGlow)"/>
    <polygon points="0,135 345,135 535,465 445,613 0,613" fill="var(--orange)"/>
    <polygon points="600,430 902,430 902,613 485,613" fill="var(--orange)"/>
    <polygon points="615,452 902,452 902,613 510,613" fill="var(--blue)"/>
  </svg>

  <svg class="abs" style="left:0;top:0;width:560px;height:381px" viewBox="0 0 902 613" preserveAspectRatio="none" role="img" aria-label="Photo of a blue two-storey family home with a white garage and landscaped front lawn">
    <defs>
      <linearGradient id="homePhoto" x1="0" y1="0" x2="0" y2="1">
        <stop offset="0" stop-color="#7fa4c2"/>
        <stop offset="0.55" stop-color="#6f8ca6"/>
        <stop offset="0.8" stop-color="#7c9a5a"/>
        <stop offset="1" stop-color="#b9bcb8"/>
      </linearGradient>
    </defs>
    <polygon points="0,158 330,158 510,465 420,613 0,613" fill="url(#homePhoto)"/>
  </svg>

  <div class="abs brand">
    <div class="brand-name">BrelloVane</div>
    <div class="brand-tagline">Heating • Cooling • Electrical • Plumbing</div>
  </div>

  <div class="abs hero hero-kicker">A LITTLE NOTE</div>
  <div class="abs hero hero-title hero-title--first">THANK</div>
  <div class="abs hero hero-title hero-title--second">YOU!</div>
  <div class="abs hero hero-quote">for welcoming our crew<br>into your home this season</div>
  <div class="abs hero hero-note">Your kind words and referrals<br>mean the world to all of us</div>

  <div class="abs signoff">
    <div class="signoff-label">With gratitude,</div>
    <div class="signoff-number">306-555-0142</div>
  </div>
</section>

<section class="card card--back" aria-label="Postcard back">
  <svg class="card-shapes" viewBox="0 0 902 613" preserveAspectRatio="none" aria-hidden="true">
    <path d="M0,480 H640 Q688,480 712,518 L775,613 H0 Z" fill="var(--orange)"/>
    <path d="M0,502 H628 Q668,502 690,538 L738,613 H0 Z" fill="var(--blue)"/>
  </svg>

  <div class="abs message">
    <h2 class="section-title">A NOTE <strong>FOR YOU</strong></h2>
  </div>
  <div class="abs message-line" style="top:76px"></div>
  <div class="abs message-line" style="top:102px"></div>
  <div class="abs message-line" style="top:128px"></div>
  <div class="abs message-line" style="top:154px"></div>
  <div class="abs message-line" style="top:180px"></div>
  <div class="abs message-line" style="top:206px"></div>
  <div class="abs message-line" style="top:232px"></div>
  <div class="abs message-line" style="top:258px"></div>

  <div class="abs divider"></div>

  <div class="abs stamp" aria-label="Stamp area"></div>
  <div class="abs address-line" style="top:165px"></div>
  <div class="abs address-line" style="top:202px"></div>
  <div class="abs address-line" style="top:239px"></div>
  <div class="abs address-line" style="top:276px"></div>

  <div class="abs signoff">
    <div class="signoff-label">Here whenever you need us</div>
    <div class="signoff-number">306-555-0142</div>
  </div>

  <div class="abs brand brand--small">
    <div class="brand-name">BrelloVane</div>
    <div class="brand-tagline">Heating • Cooling • Electrical • Plumbing</div>
  </div>
</section>

</body>
</html>
```